AK MERIDEL BUSINESS CARD DESIGN PROJECT

We need to utilize our logo that was expertly created on Markvelloo and now need to match this with a business card design.

```html
<!DOCTYPE html>
<html lang="en">
<head>
<meta charset="utf-8">
<title>AK Meridel Business Card</title>
<link rel="stylesheet" href="https://fonts.googleapis.com/css2?family=Montserrat:wght@400;500;700;800&display=swap">
<style>
  :root {
    --brand-blue: #1158ac;
    --card-white: #ffffff;
    --card-black: #161616;
    --backdrop: #e4e4e4;
    --text-light: #ffffff;
  }
  * { margin: 0; padding: 0; box-sizing: border-box; }
  html, body {
    width: 1200px;
    height: 900px;
    overflow: hidden;
    background: var(--backdrop);
    font-family: "Montserrat", sans-serif;
  }
  .canvas {
    position: relative;
    width: 1200px;
    height: 900px;
  }
  .card {
    position: absolute;
    width: 620px;
    height: 354px;
    border-radius: 22px;
    overflow: hidden;
    box-shadow: 0 10px 28px rgba(0, 0, 0, 0.22);
  }
  .card-front {
    left: 120px;
    top: 70px;
    background: var(--brand-blue);
    display: flex;
    align-items: center;
    justify-content: center;
  }
  .wordmark {
    font-family: "Montserrat", sans-serif;
    font-weight: 800;
    letter-spacing: 0.08em;
    white-space: nowrap;
  }
  .card-front .wordmark {
    color: var(--card-white);
    font-size: 62px;
  }
  .card-back {
    left: 460px;
    top: 470px;
    background: var(--card-white);
  }
  .card-back .swoosh {
    position: absolute;
    inset: 0;
    width: 100%;
    height: 100%;
  }
  .card-back .wordmark {
    position: absolute;
    right: 34px;
    top: 58px;
    color: var(--brand-blue);
    font-size: 36px;
  }
  .contact {
    position: absolute;
    left: 40px;
    top: 150px;
    color: var(--text-light);
  }
  .contact-name {
    color: var(--brand-blue);
    font-weight: 800;
    font-size: 20px;
    letter-spacing: 0.02em;
    line-height: 1.1;
  }
  .contact-title {
    font-size: 15px;
    font-weight: 500;
    margin-top: 3px;
  }
  .contact-address {
    font-size: 15px;
    font-weight: 500;
    line-height: 1.3;
    margin-top: 16px;
  }
  .contact-list {
    list-style: none;
    margin-top: 12px;
    font-size: 15px;
    font-weight: 500;
  }
  .contact-list li {
    display: flex;
    align-items: center;
    gap: 8px;
    line-height: 1.4;
  }
  .contact-icon {
    width: 12px;
    height: 12px;
    flex: none;
    fill: var(--brand-blue);
  }
</style>
</head>
<body>
<main class="canvas">

  <section class="card card-front" aria-label="Business card front">
    <span class="wordmark">AK MERIDEL</span>
  </section>

  <section class="card card-back" aria-label="Business card back">
    <svg class="swoosh" viewBox="0 0 620 354" preserveAspectRatio="none" aria-hidden="true">
      <path d="M0 26 C 180 30, 380 -8, 490 20 C 540 32, 570 50, 600 70 L 620 82 L 620 354 L 0 354 Z" fill="var(--brand-blue)" transform="translate(0,104)"/>
      <path d="M0 34 C 180 36, 380 4, 488 30 C 535 42, 565 58, 595 80 L 620 96 L 620 354 L 0 354 Z" fill="var(--card-white)" transform="translate(0,104)"/>
      <path d="M0 38 C 180 40, 380 8, 486 34 C 532 46, 562 62, 592 84 L 620 102 L 620 354 L 0 354 Z" fill="var(--card-black)" transform="translate(0,104)"/>
    </svg>

    <span class="wordmark">AK MERIDEL</span>

    <div class="contact">
      <p class="contact-name">DANIEL REYES</p>
      <p class="contact-title">Managing Director</p>
      <p class="contact-address">Your address, City<br>State, Zip 1234</p>
      <ul class="contact-list">
        <li>
          <svg class="contact-icon" viewBox="0 0 12 12" aria-hidden="true"><path d="M1 4 C1 2 3 1 6 1 C9 1 11 2 11 4 L8.5 5 L8 3.6 C7 3.3 5 3.3 4 3.6 L3.5 5 Z M2.5 6 L9.5 6 L10.5 11 L1.5 11 Z"/></svg>
          123 456 789
        </li>
        <li>
          <svg class="contact-icon" viewBox="0 0 12 12" aria-hidden="true"><path d="M0 2 L12 2 L6 7 Z M0 3.5 L6 8.5 L12 3.5 L12 10 L0 10 Z"/></svg>
          info@yourgmail.com
        </li>
        <li>
          <svg class="contact-icon" viewBox="0 0 12 12" aria-hidden="true"><circle cx="6" cy="6" r="5.5"/></svg>
          www.yourwebsite.com
        </li>
      </ul>
    </div>
  </section>

</main>
</body>
</html>
```